Business Cards that are elegant and wow

I want to create and print business cards that represent my brand and stand out from the rest. We want to ensure they stay in our branding and the integrity is not lost. I am happy to look at different shapes like square etc.

It will be printed on very thick cards and will be stylish .

I want to create and print business cards that represent my brand and stand out from the rest. We want to ensure they stay in ur branding and the integrity is not lost. I am happy to look at different shapes like square etc.

Target Market(s)

real estate professionals

Industry/Entity Type

Real Estate

Contact Information for Business Card

Maren Holt
hello@brightfernrealty.com.au
brightfernrealty.com.au
0487 316 252 (SMS)

Colors

Designer to choose colors to be used in the design.

Requirements
Must have
• My logo
• email
• website
• Name
Nice to have
• I like the idea of printing with foil or spot gloss. You want it to stand out in a sea.
Should not have
• I would like you to stay in my colour themes. Don't change the colour of my logo

```html
<!DOCTYPE html>
<html lang="en">
<head>
<meta charset="utf-8">
<title>Bright Fern Realty – Business Cards</title>
<link rel="stylesheet" href="https://fonts.googleapis.com/css2?family=Source+Sans+3:wght@400;600;700&display=swap">
<style>
  :root {
    --canvas-bg: #d9d9d9;
    --card-white: #ffffff;
    --brand-pink: #ec2f7e;
    --brand-pink-soft: #ee5b92;
    --brand-blue: #35ade3;
    --brand-blue-soft: #62bbe8;
    --ink: #1f1f1f;
  }
  * { margin: 0; padding: 0; box-sizing: border-box; }
  html, body {
    width: 1200px;
    height: 1000px;
    overflow: hidden;
    background: var(--canvas-bg);
    font-family: "Source Sans 3", "Source Sans Pro", sans-serif;
  }
  .canvas {
    position: relative;
    width: 1200px;
    height: 1000px;
  }
  .card {
    position: absolute;
    left: 346px;
    width: 516px;
    height: 295px;
    background: var(--card-white);
    overflow: hidden;
  }
  .card--front { top: 195px; }
  .card--back { top: 521px; }
  .card__art {
    position: absolute;
    inset: 0;
    width: 516px;
    height: 295px;
  }
  .contact {
    position: absolute;
    left: 18px;
    right: 18px;
    top: 76px;
    text-align: center;
    color: var(--ink);
  }
  .contact__name {
    font-size: 32px;
    font-weight: 700;
    line-height: 32px;
    letter-spacing: 0.2px;
  }
  .contact__divider {
    display: block;
    width: 244px;
    height: 4px;
    margin: 20px auto 22px;
    background: var(--brand-pink-soft);
  }
  .contact__lines {
    list-style: none;
    font-size: 18px;
    font-weight: 400;
    line-height: 23px;
  }
  .brand {
    position: absolute;
    left: 0;
    right: 0;
    top: 108px;
    display: flex;
    justify-content: center;
    align-items: center;
    gap: 16px;
  }
  .brand__mark {
    flex: 0 0 auto;
    width: 76px;
    height: 76px;
    border: 4px solid var(--brand-pink);
    border-radius: 50%;
  }
  .brand__name {
    white-space: nowrap;
    font-size: 30px;
    font-weight: 600;
    letter-spacing: 1px;
    color: var(--brand-blue);
    line-height: 1;
  }
</style>
</head>
<body>
<main class="canvas">

  <section class="card card--front" aria-label="Business card front">
    <svg class="card__art" viewBox="0 0 516 295" aria-hidden="true">
      <defs>
        <linearGradient id="pinkFrame" x1="0" y1="0" x2="1" y2="1">
          <stop offset="0" stop-color="var(--brand-pink)"/>
          <stop offset="0.5" stop-color="var(--brand-pink-soft)"/>
          <stop offset="1" stop-color="var(--brand-pink)"/>
        </linearGradient>
      </defs>
      <rect width="516" height="295" fill="url(#pinkFrame)"/>
      <polygon fill="var(--brand-blue-soft)"
        points="104,0 352,0 340,18 112,18 18,116 18,277 110,277 100,295 0,295 0,124"/>
      <polygon fill="var(--brand-blue)" points="0,124 104,0 110,0 6,124 0,130"/>
      <polygon fill="var(--brand-blue)" points="516,168 516,295 406,295"/>
      <polygon fill="var(--card-white)"
        points="112,18 498,18 498,172 410,277 18,277 18,116"/>
      <polyline fill="none" stroke="var(--brand-pink)" stroke-width="4"
        points="498,172 410,277"/>
    </svg>
    <div class="contact">
      <h1 class="contact__name">Maren Holt</h1>
      <span class="contact__divider" role="img" aria-label="Decorative pink divider"></span>
      <ul class="contact__lines">
        <li>0487 316 252 (SMS)</li>
        <li>hello@brightfernrealty.com.au</li>
        <li>brightfernrealty.com.au</li>
      </ul>
    </div>
  </section>

  <section class="card card--back" aria-label="Business card back">
    <svg class="card__art" viewBox="0 0 516 295" aria-hidden="true">
      <polygon fill="var(--brand-blue)" points="0,0 112,0 0,124"/>
      <polygon fill="var(--brand-pink)" points="112,0 118,0 0,134 0,124"/>
      <polygon fill="var(--brand-blue)" points="516,162 516,170 404,295 396,295"/>
      <polygon fill="var(--brand-pink)" points="516,174 516,295 408,295"/>
    </svg>
    <div class="brand">
      <span class="brand__mark" aria-hidden="true"></span>
      <span class="brand__name">BRIGHT FERN REALTY</span>
    </div>
  </section>

</main>
</body>
</html>
```